Landing Page Design for Business Page

I need a very attractive landing page designed for my business to obtain customer information. I would like an improvement to an existing landing page we have that is much more appealing and modern.

I have included resources and assets in the below Google Drive folder. I am a big fan of some of the imagery in the "Banners" folder for design.

https://files.plorvex.net/share/7kTqw52LmbHxZpe3Ra9-nVdWUcFs8yJ?mode=view

Here is existing landing page that I would like improved upon.

http://lp4.vurmalpower.net/vmp-lx-signup

```html
<!DOCTYPE html>
<html lang="en">
<head>
<meta charset="utf-8">
<title>Vurmal Power – Home Energy Savings</title>
<link href="https://fonts.googleapis.com/css2?family=Bebas+Neue&family=Open+Sans:wght@400;600;700&display=swap" rel="stylesheet">
<style>
:root{
  --blue:#3cb5ea;
  --green:#5cb82e;
  --navy:#0d3366;
  --footer:#0b2447;
  --text:#333a44;
  --field:#eef1f5;
  --white:#ffffff;
}
*{box-sizing:border-box;margin:0;padding:0}
html,body{width:1200px;height:3757px;overflow:hidden}
body{position:relative;background:var(--white);font-family:'Open Sans',sans-serif;color:var(--text)}
.abs{position:absolute}
.display{font-family:'Bebas Neue',sans-serif;font-weight:400;letter-spacing:.5px}
.center{text-align:center}

/* top bar */
.topbar{left:0;top:0;width:1200px;height:45px;background:linear-gradient(90deg,var(--blue),#7fb3c9 60%,#9a8f7e)}
.topbar-cta{left:0;top:0;width:1200px;line-height:45px;color:var(--white);font-size:21px}
.callbox{left:921px;top:0;width:279px;height:45px;background:var(--green);color:var(--white);display:flex;align-items:center;gap:8px;padding-left:22px}
.callbox small{font-size:12px}
.callbox strong{font-family:'Bebas Neue',sans-serif;font-weight:400;font-size:27px;letter-spacing:.5px}

/* header */
.hero-photo{left:0;top:0;width:1200px;height:678px;clip-path:polygon(0 0,100% 0,100% 532px,0 678px);
  background:linear-gradient(180deg,rgba(70,176,228,.9) 0%,rgba(93,184,47,.85) 55%,rgba(98,182,40,.9) 100%),linear-gradient(90deg,#6fb14a 0%,#a88a5f 70%,#b78d5f 100%)}
.hero-wood{left:620px;top:45px;width:580px;height:600px;clip-path:polygon(0 0,100% 0,100% 487px,0 558px);background:linear-gradient(90deg,rgba(140,170,90,0),rgba(176,140,96,.85) 35%,#b88f63 100%)}
.header{left:36px;top:45px;width:1126px;height:75px;background:var(--white)}
.brand{display:flex;align-items:center;gap:10px;color:var(--navy);font-family:'Bebas Neue',sans-serif;font-size:34px;line-height:1;white-space:nowrap}
.brand i{width:14px;height:14px;background:var(--navy);display:block}
.nav{font-family:'Bebas Neue',sans-serif;font-size:16px;color:var(--navy)}
.nav span{position:absolute;white-space:nowrap}
.search{left:921px;top:70px;width:199px;height:29px;background:var(--field);font-size:11px;color:#666;padding:7px 0 0 20px;font-style:italic}
.search-btn{left:1120px;top:70px;width:28px;height:29px;background:var(--navy)}

.hero-title{left:65px;top:250px;width:600px;color:var(--white);font-size:48px;line-height:46px}
.hero-sub{left:65px;top:402px;width:600px;color:var(--white);font-size:13px;font-weight:600}
.btn{display:flex;align-items:center;justify-content:center;color:var(--white);font-family:'Bebas Neue',sans-serif;font-size:15px;letter-spacing:.5px}
.btn-navy{background:var(--navy)}
.btn-green{background:var(--green)}
.dots{left:568px;top:544px;display:flex;gap:8px}
.dots i{width:7px;height:7px;border:1px solid var(--white);border-radius:50%;display:block}
.dots i.on{background:var(--white)}
.badge{border-radius:50%;background:rgba(255,255,255,.85)}

/* about */
.eyebrow{font-size:10px;letter-spacing:4px;font-weight:600}
.h2{color:var(--navy);font-size:54px;line-height:1}
.copy{font-size:11px;line-height:17px;color:var(--text)}
.thumb{width:232px;height:152px}
.icon-ring{width:76px;height:76px;border-radius:50%;background:var(--blue);border:4px solid var(--white);display:flex;align-items:center;justify-content:center}
.card-title{width:290px;color:var(--navy);font-size:27px;text-align:center}
.rule{height:1px;background:#dde2e8}

/* qualify */
.qualify-bg{left:0;top:1330px;width:1200px;height:420px;background:linear-gradient(180deg,var(--blue) 0%,#52b7b4 35%,var(--green) 75%)}
.qualify-photo{left:0;top:1330px;width:420px;height:420px;clip-path:polygon(0 0,378px 0,420px 100%,0 100%);background:linear-gradient(160deg,#8f9195,#c9c6bf 55%,#6f7276)}
.qualify-title{left:520px;top:1393px;width:560px;color:var(--white);font-size:46px;line-height:46px}
.qualify-title b{font-weight:400;color:var(--navy)}
.field{background:var(--white);font-size:11px;color:#555;padding:0 15px;display:flex;align-items:center}

/* services */
.services-bg{left:0;top:1758px;width:1200px;height:591px;background:linear-gradient(180deg,#3eaadb 0%,#4fb2a6 40%,var(--green) 85%)}
.svc-img{width:297px;height:174px}
.svc-title{width:297px;color:var(--white);font-size:26px;text-align:center}
.svc-copy{width:260px;color:var(--white);font-size:10.5px;line-height:17px;text-align:center}

/* how we work */
.work-bg{left:0;top:2349px;width:1200px;height:545px;background:linear-gradient(180deg,var(--white) 0%,#e6ebf2 100%)}
.step-card{width:305px;height:280px;background:var(--white);clip-path:polygon(0 0,100% 0,100% 90%,0 100%);padding:64px 38px 0;font-size:10.5px;line-height:17px;text-align:center;color:var(--text)}
.step-badge{width:76px;height:76px;border-radius:50%;background:var(--blue);border:4px solid var(--white);color:var(--white);text-align:center;line-height:1}
.step-badge small{display:block;font-family:'Bebas Neue',sans-serif;font-size:14px;margin-top:10px}
.step-badge strong{display:block;font-family:'Bebas Neue',sans-serif;font-weight:400;font-size:40px;color:var(--navy)}

/* estimate */
.estimate-title{left:0;top:2970px;width:1200px;color:var(--navy);font-size:50px;line-height:48px}
.estimate-title em{font-style:normal;color:var(--blue)}
.field-grey{background:var(--field)}

/* footer */
.footer{left:0;top:3237px;width:1200px;height:520px;background:var(--footer);clip-path:polygon(0 102px,100% 0,100% 100%,0 100%)}
.foot-head{font-size:10px;color:var(--blue);font-weight:600}
.foot-list{font-size:11px;color:var(--white);line-height:31px}
.foot-info{font-size:11px;color:var(--white);line-height:17px}
.foot-rule{left:0;top:3689px;width:1200px;height:1px;background:rgba(255,255,255,.15)}
.copyright{left:0;top:3703px;width:1200px;color:var(--white);font-size:15px}
</style>
</head>
<body>

<!-- HERO -->
<div class="abs hero-photo" role="img" aria-label="Technician blowing insulation between wooden wall studs, under a blue to green overlay"></div>
<div class="abs hero-wood" role="img" aria-label="Insulation hose and wooden framing"></div>

<div class="abs topbar"></div>
<div class="abs topbar-cta display center">Schedule your no-cost assessment now</div>
<div class="abs callbox">
  <small>Call us at:</small>
  <svg width="18" height="18" viewBox="0 0 24 24"><circle cx="12" cy="12" r="11" fill="none" stroke="#fff" stroke-width="1.5"/><path d="M8 6.5l2 0 1 3-1.3 1a7 7 0 0 0 3.8 3.8l1-1.3 3 1v2c0 .6-.5 1-1 1A10 10 0 0 1 7 7.5c0-.5.4-1 1-1z" fill="#fff"/></svg>
  <strong>555-204-7391</strong>
</div>

<header class="abs header">
  <div class="abs brand" style="left:18px;top:22px"><i></i>Vurmal Power</div>
</header>
<nav class="abs nav" style="left:0;top:78px">
  <span style="left:322px">Home</span>
  <span style="left:394px">Services ⌄</span>
  <span style="left:500px">Rebates</span>
  <span style="left:588px">About Us</span>
  <span style="left:681px">Covid 19</span>
  <span style="left:765px">Employees ⌄</span>
</nav>
<div class="abs search">Search...</div>
<div class="abs search-btn">
  <svg width="28" height="29" viewBox="0 0 28 29"><circle cx="13" cy="13" r="5" fill="none" stroke="#fff" stroke-width="2"/><path d="M17 17l4 4" stroke="#fff" stroke-width="2"/></svg>
</div>

<h1 class="abs hero-title display center">We can help you save on your<br>energy bills by improving your<br>energy efficiency</h1>
<p class="abs hero-sub center">Contact Vurmal Power for a no-cost, no-obligation estimate today</p>
<a class="abs btn btn-navy" style="left:308px;top:443px;width:116px;height:29px">Contact Us</a>
<div class="abs dots"><i></i><i class="on"></i><i></i><i></i><i></i></div>
<div class="abs badge" style="left:1000px;top:420px;width:80px;height:80px;opacity:.55"></div>

<!-- ABOUT -->
<p class="abs eyebrow center" style="left:0;top:692px;width:1200px;color:var(--green)">About</p>
<h2 class="abs h2 display center" style="left:0;top:712px;width:1200px">Vurmal Power</h2>
<div class="abs copy center" style="left:230px;top:776px;width:740px">
  <p>Vurmal Power is a small, locally owned business in Fairhaven, Massachusetts.</p>
  <p style="margin-top:16px">If you're a homeowner, commercial or residential landlord, we provide a solution to reduce your energy costs, both heating and electrical. We provide a free, no-obligation assessment for your home.</p>
  <p style="margin-top:16px">Following the assessment, we will make suggestions to improve its energy efficiency including but not limited to:</p>
</div>

<div class="abs thumb" style="left:99px;top:920px;background:linear-gradient(135deg,#6b7a72,#c9b7a8 50%,#7c9a5c)" role="img" aria-label="Worker carrying rolls of wall insulation"></div>
<div class="abs thumb" style="left:356px;top:920px;background:linear-gradient(135deg,#4d5c5f,#a9b2a4 50%,#3f6a3a)" role="img" aria-label="Crew unloading equipment by a house garage"></div>
<div class="abs thumb" style="left:612px;top:920px;background:linear-gradient(135deg,#5a3a22,#c5a27e 50%,#7a4a28)" role="img" aria-label="Attic insulation being blown in"></div>
<div class="abs thumb" style="left:869px;top:920px;background:linear-gradient(135deg,#4a3526,#b08867 50%,#6e5039)" role="img" aria-label="Sealing gaps around attic framing"></div>

<div class="abs icon-ring" style="left:177px;top:1034px"><svg width="38" height="38" viewBox="0 0 38 38" fill="none" stroke="#fff" stroke-width="2"><path d="M4 18L19 6l15 12"/><path d="M9 15v16h20V15"/><path d="M14 31v-9h10v9"/></svg></div>
<div class="abs icon-ring" style="left:434px;top:1034px"><svg width="38" height="38" viewBox="0 0 38 38" fill="none" stroke="#fff" stroke-width="2"><path d="M4 18L19 6l15 12"/><rect x="9" y="16" width="20" height="15"/><path d="M19 16v15M9 23h20"/></svg></div>
<div class="abs icon-ring" style="left:690px;top:1034px"><svg width="38" height="38" viewBox="0 0 38 38" fill="none" stroke="#fff" stroke-width="2"><path d="M19 5L5 31h28z"/><path d="M12 19h14M9 25h20"/></svg></div>
<div class="abs icon-ring" style="left:947px;top:1034px"><svg width="38" height="38" viewBox="0 0 38 38" fill="none" stroke="#fff" stroke-width="2"><path d="M5 15h20a4 4 0 1 0-4-4"/><path d="M5 21h26a4 4 0 1 1-4 4"/><path d="M8 27h10"/></svg></div>

<h3 class="abs card-title display" style="left:70px;top:1122px">Wall Insulation</h3>
<h3 class="abs card-title display" style="left:327px;top:1122px">General Construction</h3>
<h3 class="abs card-title display" style="left:583px;top:1122px">Attic Insulation</h3>
<h3 class="abs card-title display" style="left:840px;top:1122px">Air Sealing</h3>

<div class="abs rule" style="left:268px;top:1228px;width:230px"></div>
<div class="abs rule" style="left:704px;top:1228px;width:230px"></div>
<a class="abs btn btn-green" style="left:541px;top:1214px;width:118px;height:30px">Learn More</a>

<!-- QUALIFY -->
<section>
  <div class="abs qualify-bg" role="img" aria-label="Service trucks parked outside, under a blue to green overlay"></div>
  <div class="abs qualify-photo" role="img" aria-label="Respirator mask resting on a diamond-plate truck bed"></div>
  <h2 class="abs qualify-title display center">Do I qualify for<br><b>75-100% off</b><br>insulation &amp; weatherization?</h2>
  <div class="abs field" style="left:537px;top:1551px;width:255px;height:30px">First Name:</div>
  <div class="abs field" style="left:802px;top:1551px;width:255px;height:30px">Last Name:</div>
  <div class="abs field" style="left:537px;top:1594px;width:166px;height:30px">Phone:</div>
  <div class="abs field" style="left:713px;top:1594px;width:167px;height:30px">Email:</div>
  <div class="abs field" style="left:890px;top:1594px;width:167px;height:30px">City:</div>
  <a class="abs btn btn-navy" style="left:739px;top:1650px;width:117px;height:30px">Submit Form</a>
</section>

<!-- SERVICES -->
<section>
  <div class="abs services-bg" role="img" aria-label="Technician working in an attic, under a blue to green overlay"></div>
  <p class="abs eyebrow center" style="left:0;top:1838px;width:1200px;color:var(--white)">What we do</p>
  <h2 class="abs h2 display center" style="left:0;top:1860px;width:1200px;color:var(--white)">Our Services</h2>

  <div class="abs svc-img" style="left:99px;top:1933px;background:linear-gradient(135deg,#3b2a1c,#b08a5e 55%,#4a3422)" role="img" aria-label="Technician inspecting an attic with a flashlight"></div>
  <div class="abs svc-img" style="left:452px;top:1933px;background:linear-gradient(135deg,#5b3423,#d3a782 50%,#7a4a30)" role="img" aria-label="Attic floor with insulation and air sealing"></div>
  <div class="abs svc-img" style="left:803px;top:1933px;background:linear-gradient(135deg,#c7b6aa,#8a7b78 50%,#2c3d52)" role="img" aria-label="Hands holding a phone for a virtual assessment"></div>

  <h3 class="abs svc-title display" style="left:99px;top:2133px">Home Energy Assessments</h3>
  <h3 class="abs svc-title display" style="left:452px;top:2133px">Insulation &amp; Air Sealing</h3>
  <h3 class="abs svc-title display" style="left:803px;top:2133px">Virtual Assessments</h3>

  <p class="abs svc-copy" style="left:118px;top:2170px">Save energy, save money and keep Mass. green with a no-cost HomeSave® home energy assessment. Offering virtual and in-home assessments to customers across Massachusetts, from Western MA to Cape Cod.</p>
  <p class="abs svc-copy" style="left:470px;top:2170px">Save energy, save money and keep Mass. green with a no-cost HomeSave® home energy assessment. Offering virtual and in-home assessments to customers across Massachusetts, from Western MA to Cape Cod.</p>
  <p class="abs svc-copy" style="left:822px;top:2170px">Save energy, save money and keep Mass. green with a no-cost HomeSave® home energy assessment. Offering virtual and in-home assessments to customers across Massachusetts, from Western MA to Cape Cod.</p>
</section>

<!-- HOW WE WORK -->
<section>
  <div class="abs work-bg"></div>
  <h2 class="abs h2 display center" style="left:0;top:2432px;width:1200px">How We Work</h2>

  <div class="abs step-card" style="left:99px;top:2549px">We begin our journey with you by performing an in-home audit. A member of our team, a fully qualified technician, will schedule a time that works for you to come and assess your home. The assessment will include various tests to decide how best to make your home more energy-efficient.</div>
  <div class="abs step-card" style="left:447px;top:2549px">Following the in-home audit, Vurmal Power will provide you with a written evaluation of how your home's energy efficiency can be improved. In that evaluation, we will include the cost after any incentives or discounts that you are eligible for, and a form to confirm whether you would like to work with us to improve your home's energy efficiency using insulation and weatherization tools.</div>
  <div class="abs step-card" style="left:795px;top:2549px">After receiving your request to start work, a member of our team will contact you to schedule the work appointment. Our team will perform the work agreed upon in the evaluation, and leave your home more energy efficient!</div>

  <div class="abs step-badge" style="left:210px;top:2509px"><small>Step</small><strong>1</strong></div>
  <div class="abs step-badge" style="left:562px;top:2509px"><small>Step</small><strong>2</strong></div>
  <div class="abs step-badge" style="left:913px;top:2509px"><small>Step</small><strong>3</strong></div>
</section>

<!-- ESTIMATE -->
<section>
  <h2 class="abs estimate-title display center">Get your<br><em>Free</em> home energy savings <em>estimate</em> today!</h2>
  <div class="abs copy center" style="left:240px;top:3084px;width:720px;font-size:10.5px">
    <p><strong>To receive a no-obligation, NO-COST estimate,</strong></p>
    <p><strong>Please fill out the form below and a member of Vurmal Power will be in touch with you!</strong> You'll be one step closer to improving your energy efficiency, and lowering your energy bills.</p>
  </div>
  <div class="abs field field-grey" style="left:295px;top:3164px;width:255px;height:30px">Name:</div>
  <div class="abs field field-grey" style="left:558px;top:3164px;width:256px;height:30px">Email:</div>
  <a class="abs btn btn-green" style="left:824px;top:3164px;width:80px;height:30px">Send</a>
</section>

<!-- FOOTER -->
<footer>
  <div class="abs footer"></div>
  <div class="abs brand" style="left:103px;top:3460px;color:var(--white);font-size:44px"><i style="background:var(--white);width:18px;height:18px"></i>Vurmal Power</div>

  <p class="abs foot-head" style="left:480px;top:3394px">NAVIGATION</p>
  <div class="abs foot-list" style="left:480px;top:3419px">
    <p>HOME</p><p>SERVICES ⌄</p><p>REBATES</p><p>ABOUT US</p><p>Covid 19</p><p>Employees ⌄</p>
  </div>

  <p class="abs foot-head" style="left:709px;top:3394px">CONTACT US</p>
  <div class="abs foot-info" style="left:709px;top:3427px">
    <p>Email:<br>info@vurmalpower.net</p>
    <p style="margin-top:14px">Phone:<br>555-204-7391</p>
    <p style="margin-top:14px">Address<br>42 Harbor Lane, Suite 3B,<br>Fairhaven, MA 02719</p>
  </div>

  <div class="abs badge" style="left:1006px;top:3400px;width:84px;height:84px;opacity:.9"></div>

  <div class="abs foot-rule"></div>
  <p class="abs copyright display center">Vurmal Power © 2022. All rights reserved</p>
</footer>

</body>
</html>
```